Esthetically Pleasing Core Values and Brand Promise for Accounting Firm

I would like a cohesive design that ties together my core values and brand promise. My firm, Maple Finch Advisory, provides accounting work to small businesses. I prefer modern and clean designs. I want my Core Values and Brand Promise to represent me - sole entrepreneur, married, mother of two kids, modern esthetics, clean lines, organized, colorful (teals, greys, white, yellows)

Industry/Entity Type

Public Accounting

Colors
33b8a4

```html
<!DOCTYPE html>
<html lang="en">
<head>
<meta charset="utf-8">
<title>Maple Finch Advisory – Core Values</title>
<link href="https://fonts.googleapis.com/css2?family=Montserrat:wght@400;700;800&family=Roboto+Condensed:wght@400;700&display=swap" rel="stylesheet">
<style>
  :root {
    --bg: #e9eaea;
    --paper: #ffffff;
    --teal: #33b8a4;
    --teal-mid: #26a08f;
    --teal-deep: #176b60;
    --teal-pale: #bfe6df;
    --ink: #3a3a3a;
    --grey: #6d6d6d;
    --photo-a: #dfe7ee;
    --photo-b: #b9cbdc;
  }
  * { box-sizing: border-box; margin: 0; padding: 0; }
  html, body { width: 1200px; height: 801px; overflow: hidden; background: var(--bg); }
  .flyer {
    position: absolute; left: 330px; top: 20px; width: 540px; height: 760px;
    background: var(--paper); overflow: hidden;
    box-shadow: 0 6px 24px rgba(0,0,0,.12);
    font-family: "Roboto Condensed", Arial, sans-serif; color: var(--ink);
  }
  .photo {
    position: absolute; left: 0; top: 0; width: 540px; height: 320px;
    background: linear-gradient(135deg, var(--photo-a) 0%, var(--photo-b) 55%, #d9e2ea 100%);
  }
  .waves { position: absolute; left: 0; top: 0; }
  .brand-panel {
    position: absolute; left: 22px; top: 140px; width: 200px; height: 86px;
    background: rgba(255,255,255,.78); border-radius: 10px;
    display: flex; align-items: center; gap: 10px; padding: 0 14px;
  }
  .brand-dot { width: 22px; height: 22px; border-radius: 50%; background: var(--teal); flex: none; }
  .brand-name {
    font-family: "Montserrat", Arial, sans-serif; font-weight: 400; font-size: 19px;
    line-height: 1.15; color: var(--teal-mid); letter-spacing: 1px;
  }
  .section-title {
    position: absolute; left: 34px; top: 296px;
    font-family: "Montserrat", Arial, sans-serif; font-weight: 800; font-size: 31px;
    line-height: 1.02; color: #fff;
  }
  .value-card {
    position: absolute; width: 114px; height: 218px;
    background: linear-gradient(180deg, var(--teal-mid), var(--teal-deep));
    border: 3px solid #fff; border-radius: 57px 57px 40px 40px;
    color: #fff; text-align: center; padding: 12px 9px 12px;
    box-shadow: 0 3px 8px rgba(0,0,0,.15);
  }
  .value-icon {
    width: 50px; height: 50px; margin: 0 auto; border: 2px solid #fff; border-radius: 50%;
    display: flex; align-items: center; justify-content: center;
  }
  .value-name { font-weight: 700; font-size: 13.5px; line-height: 1.2; margin-top: 7px; }
  .value-rule { height: 1px; background: rgba(255,255,255,.7); margin: 5px 8px 6px; }
  .value-text { font-size: 11px; line-height: 1.25; }
  .promise {
    position: absolute; left: 36px; top: 620px; width: 468px; height: 30px;
    border: 1.5px solid var(--ink); display: flex; align-items: center; justify-content: center;
    font-weight: 700; font-size: 14px; letter-spacing: .2px;
  }
  .service { position: absolute; top: 660px; width: 220px; text-align: center; }
  .service-title { font-family: "Montserrat", Arial, sans-serif; font-weight: 700; font-size: 18px; line-height: 1.2; }
  .service-text { font-size: 11px; line-height: 1.3; color: var(--grey); margin-top: 3px; }
  .tax { left: 40px; }
  .accounting { left: 280px; }
  .foot-band { position: absolute; left: 0; bottom: 0; width: 540px; height: 10px; background: var(--teal-mid); }
</style>
</head>
<body>
  <main class="flyer">
    <div class="photo" role="img" aria-label="Photo of an accountant working a calculator over paperwork"></div>

    <svg class="waves" width="540" height="620" viewBox="0 0 540 620" aria-hidden="true">
      <path d="M0 260 C180 250 360 160 540 70 L540 120 C380 210 200 280 0 300 Z" fill="var(--teal-pale)" opacity=".85"/>
      <path d="M0 280 C180 272 370 180 540 95 L540 450 C380 515 200 570 0 590 Z" fill="var(--teal)"/>
      <path d="M0 590 C200 570 380 515 540 450 L540 470 C380 535 200 590 0 610 Z" fill="var(--teal-pale)"/>
    </svg>

    <div class="brand-panel">
      <span class="brand-dot"></span>
      <span class="brand-name">MAPLE FINCH<br>ADVISORY</span>
    </div>

    <h1 class="section-title">Core<br>Values</h1>

    <section class="value-card" style="left:40px; top:384px;">
      <div class="value-icon"><svg width="24" height="24" viewBox="0 0 24 24"><path d="M6 12 L10 16 L18 7" fill="none" stroke="#fff" stroke-width="2"/></svg></div>
      <h2 class="value-name">Empower</h2>
      <div class="value-rule"></div>
      <p class="value-text">we are dedicated, appreciative and respectful of people's time and purpose.</p>
    </section>

    <section class="value-card" style="left:162px; top:344px;">
      <div class="value-icon"><svg width="26" height="26" viewBox="0 0 26 26"><circle cx="13" cy="13" r="9" fill="none" stroke="#fff" stroke-width="2"/><circle cx="13" cy="13" r="3" fill="#fff"/></svg></div>
      <h2 class="value-name">Client Focused</h2>
      <div class="value-rule"></div>
      <p class="value-text">we provide a personal service that goes above the standards of professional care.</p>
    </section>

    <section class="value-card" style="left:284px; top:304px;">
      <div class="value-icon"><svg width="28" height="26" viewBox="0 0 28 26"><path d="M14 3 V22 M5 7 H23 M9 22 H19" stroke="#fff" stroke-width="2" fill="none"/><path d="M2 15 L5 7 L8 15 Z M20 15 L23 7 L26 15 Z" fill="none" stroke="#fff" stroke-width="1.5"/></svg></div>
      <h2 class="value-name">Rectitude</h2>
      <div class="value-rule"></div>
      <p class="value-text">we know the difference between what we have the right to do and what the right thing to do is.</p>
    </section>

    <section class="value-card" style="left:406px; top:264px;">
      <div class="value-icon"><svg width="20" height="24" viewBox="0 0 20 24"><path d="M12 1 L3 14 H10 L8 23 L17 10 H10 Z" fill="#fff"/></svg></div>
      <h2 class="value-name">Relentless</h2>
      <div class="value-rule"></div>
      <p class="value-text">we believe that the longer we try to do our best, the better we become.</p>
    </section>

    <div class="promise">BRAND PROMISE - TRUST, TRANSPARENCY AND DEPENDABILITY</div>

    <section class="service tax">
      <h3 class="service-title">TAX:</h3>
      <p class="service-text">Maple Finch provides all clients with a trusted tax advisor who provides accuracy in all filings and ensures your compliance with all government agencies.</p>
    </section>

    <section class="service accounting">
      <h3 class="service-title">ACCOUNTING:</h3>
      <p class="service-text">Maple Finch provides all business owners with the financial visibility needed to foster growth and facilitate goals.</p>
    </section>

    <div class="foot-band"></div>
  </main>
</body>
</html>
```